Mortgage Broking boutique Business

I’m wanting a revamped look to my existing business card design. I do like the black and silver but happy to have other colours introduced based on your creation. I’ve attached a copy of my current card so you can have a starting point updated details noted brloe. I deal with high net worth individuals so need my card to be sophisticated, classy that gives off a classy vibe

Target Market(s)

High net worth, wealthy

Industry/Entity Type

Mortgage Brokerage

Contact Information for Business Card

Job title: Finance Executive
Phone: +61 7 3287 4419
Mobile: 0471 352 608
Email: marcus@quillbrookcapital.com.au
Web: www.quillbrookcapital.com.au
Address: level 36 Tindale Court, 58 Harwick St Brisbane QLD 4000

Font styles to use
Other font styles liked:
• Helvetica

Colors

Designer to choose colors to be used in the design.

Requirements
Must have
• Use my existing card design as a starting point

```html
<!DOCTYPE html>
<html lang="en">
<head>
<meta charset="utf-8">
<title>Quillbrook Capital – Business Card</title>
<link rel="stylesheet" href="https://fonts.googleapis.com/css2?family=Montserrat:wght@400;700&family=Oswald:wght@300;500&family=Arimo:wght@400&display=swap">
<style>
  :root {
    --backdrop: #1c1c1e;
    --card: #0e0f11;
    --gold: #a8801f;
    --gold-soft: #8f6c1c;
  }
  * { margin: 0; padding: 0; box-sizing: border-box; }
  html, body { width: 1200px; height: 1200px; overflow: hidden; background: var(--backdrop); }
  .canvas { position: relative; width: 1200px; height: 1200px; }
  .card {
    position: absolute; left: 228px; width: 744px; height: 424px;
    background: var(--card);
    box-shadow: 0 10px 30px rgba(0,0,0,.55);
  }
  .card--front { top: 136px; }
  .card--back { top: 640px; }

  .brand-line {
    position: absolute; left: 42px; top: 70px;
    font-family: "Montserrat", sans-serif; font-weight: 700;
    font-size: 38px; letter-spacing: 3px; color: var(--gold);
    white-space: nowrap;
  }
  .holder-name {
    position: absolute; left: 42px; top: 160px;
    font-family: "Oswald", sans-serif; font-weight: 500;
    font-size: 52px; line-height: 1; color: var(--gold);
  }
  .holder-title {
    position: absolute; left: 42px; top: 230px;
    font-family: "Oswald", sans-serif; font-weight: 300;
    font-size: 30px; line-height: 1; color: var(--gold);
  }
  .divider {
    position: absolute; left: 42px; top: 286px;
    width: 63px; height: 4px; background: var(--gold);
  }
  .contact {
    position: absolute; left: 42px;
    font-family: "Arimo", "Helvetica", sans-serif;
    font-size: 18px; color: var(--gold); white-space: nowrap;
  }
  .contact--address { top: 318px; }
  .contact--lines { top: 354px; }

  .brand-mark {
    position: absolute; left: 312px; top: 62px;
    width: 120px; height: 120px; background: var(--gold);
  }
  .brand-stack {
    position: absolute; left: 0; right: 0; top: 200px;
    text-align: center;
    font-family: "Montserrat", sans-serif; font-weight: 700;
    font-size: 34px; line-height: 46px; letter-spacing: 4px; color: var(--gold);
  }
  .web {
    position: absolute; left: 0; right: 0; top: 378px;
    text-align: center;
    font-family: "Arimo", "Helvetica", sans-serif;
    font-size: 18px; color: var(--gold-soft); letter-spacing: .5px;
  }
</style>
</head>
<body>
<main class="canvas">
  <section class="card card--front">
    <div class="brand-line">QUILLBROOK CAPITAL</div>
    <h1 class="holder-name">MARCUS REID</h1>
    <p class="holder-title">FINANCE EXECUTIVE</p>
    <div class="divider"></div>
    <p class="contact contact--address">level 36 Tindale Court, 58 Harwick St Brisbane QLD 4000</p>
    <p class="contact contact--lines">P : +61 7 3287 4419 / M : 0471 352 608 marcus@quillbrookcapital.com.au</p>
  </section>

  <section class="card card--back">
    <div class="brand-mark"></div>
    <div class="brand-stack">QUILLBROOK<br>CAPITAL</div>
    <p class="web">WWW.QUILLBROOKCAPITAL.COM.AU</p>
  </section>
</main>
</body>
</html>
```